Business Card Design Project

I need a business card design for my freelance solo makeup artistry business in Melbourne, Australia called Rosa Fennimore. My freelance business specialises in bridal and special occassions makeup.

I like the idea of having Rosa Fennimore in pink as its a feminine and soft colour. I would like a very clean, classy and simple (with an element of fun if that's possible) design. I would consider the business name to be in gloss with an otherwise matte finish.

Underneath the business name, I would like "Makeup by Tara Quillend"

I do not want any bridal related graphics.

Target Market(s)

Young females with a disposable income from ages 20-40 and females getting married who will dictate who does mother of bride makeup ages 40-70.

Industry/Entity Type

Business

Requirements
Must have
• "Makeup by Tara Quillend"

Ph: 0432 615 204
E: rosafennimore@examplemail.com
ABN: 58902147635
Nice to have
• I think I would like a mini business cards which is more slimline. I do like the colours of pink, white and grey but open to suggestions.
Should not have
• Bridal related graphics

```html
<!DOCTYPE html>
<html lang="en">
<head>
<meta charset="utf-8">
<title>Rosa Fennimore – Business Card</title>
<link rel="stylesheet" href="https://fonts.googleapis.com/css2?family=Allura&family=Roboto:wght@300;400&display=swap">
<style>
  :root {
    --pink: #ec2b8c;
    --pink-soft: #f25aa6;
    --charcoal: #2e2e30;
    --charcoal-deep: #252527;
    --white: #ffffff;
    --stage: #d9dadc;
    --script: "Allura", cursive;
    --body: "Roboto", sans-serif;
  }
  * { box-sizing: border-box; margin: 0; padding: 0; }
  html, body { width: 1200px; height: 840px; overflow: hidden; }
  body {
    background: var(--stage);
    display: flex;
    flex-direction: column;
    align-items: center;
    justify-content: center;
    gap: 56px;
  }
  .card {
    position: relative;
    width: 600px;
    height: 343px;
    background: var(--charcoal);
    border-radius: 4px;
    overflow: hidden;
    box-shadow: 0 6px 18px rgba(0,0,0,0.18);
  }

  /* Contact side */
  .card-contact .name-band {
    position: absolute;
    inset: 0 0 auto 0;
    height: 132px;
    background: var(--pink);
  }
  .card-contact .band-edge {
    position: absolute;
    left: 0; top: 132px;
    width: 600px; height: 9px;
    display: block;
  }
  .card-contact .business-name {
    position: absolute;
    left: 36px; top: 18px;
    font-family: var(--script);
    font-size: 64px;
    color: var(--white);
    line-height: 1;
  }
  .card-contact .tagline {
    position: absolute;
    left: 62px; top: 92px;
    font-family: var(--script);
    font-size: 22px;
    color: var(--charcoal);
    line-height: 1;
  }
  .card-contact .kiss-mark {
    position: absolute;
    right: 34px; top: 46px;
    width: 78px; height: 40px;
    border-radius: 50%;
    background: radial-gradient(ellipse at center, #c81f74 0%, #d72480 60%, var(--pink) 100%);
    opacity: 0.75;
  }
  .contact-list {
    position: absolute;
    right: 40px; top: 176px;
    list-style: none;
    font-family: var(--body);
    font-weight: 300;
    font-size: 17px;
    color: var(--white);
    letter-spacing: 0.5px;
  }
  .contact-list li {
    display: flex;
    align-items: center;
    justify-content: flex-end;
    gap: 10px;
    height: 30px;
  }
  .contact-list svg { width: 15px; height: 15px; fill: var(--pink); }
  .contact-list .label {
    color: var(--pink);
    font-weight: 400;
    font-size: 15px;
    text-transform: lowercase;
  }

  /* Brand side */
  .card-brand { background: var(--charcoal-deep); }
  .card-brand .monogram {
    position: absolute;
    left: 150px; top: 24px;
    width: 260px; height: 300px;
    border-radius: 46% 54% 48% 52% / 40% 42% 58% 60%;
    background: linear-gradient(160deg, var(--pink-soft), var(--pink));
  }
  .card-brand .business-name {
    position: absolute;
    left: 60px; top: 180px;
    font-family: var(--script);
    font-size: 72px;
    color: var(--white);
    line-height: 1;
  }
</style>
</head>
<body>

  <section class="card card-contact" aria-label="Business card, contact side">
    <div class="name-band"></div>
    <svg class="band-edge" viewBox="0 0 600 9" preserveAspectRatio="none" aria-hidden="true">
      <defs>
        <pattern id="zigzag" width="10" height="9" patternUnits="userSpaceOnUse">
          <polygon points="0,0 10,0 5,9" fill="#ec2b8c"/>
        </pattern>
      </defs>
      <rect width="600" height="9" fill="url(#zigzag)"/>
    </svg>
    <h1 class="business-name">Rosa Fennimore</h1>
    <p class="tagline">makeup by Tara Quillend</p>
    <div class="kiss-mark" role="img" aria-label="Pink lipstick kiss print"></div>

    <ul class="contact-list">
      <li>
        <svg viewBox="0 0 24 24" aria-hidden="true"><path d="M6.6 10.8a15.1 15.1 0 0 0 6.6 6.6l2.2-2.2c.3-.3.7-.4 1-.2 1.1.4 2.3.6 3.6.6.6 0 1 .4 1 1V20c0 .6-.4 1-1 1A17 17 0 0 1 3 4c0-.6.4-1 1-1h3.5c.6 0 1 .4 1 1 0 1.3.2 2.5.6 3.6.1.3 0 .7-.2 1z"/></svg>
        <span>0432 615 204</span>
      </li>
      <li>
        <svg viewBox="0 0 24 24" aria-hidden="true"><path d="M2 5h20v14H2z M4 7v.5l8 5 8-5V7l-8 5z" fill-rule="evenodd"/></svg>
        <span>rosafennimore@examplemail.com</span>
      </li>
      <li>
        <span class="label">abn</span>
        <span>58902147635</span>
      </li>
    </ul>
  </section>

  <section class="card card-brand" aria-label="Business card, name side">
    <div class="monogram" role="img" aria-label="Large pink hand-lettered initial"></div>
    <p class="business-name">Rosa Fennimore</p>
  </section>

</body>
</html>
```